Bref créative
Stationary Pack
Business Cards, Letterheads, fax etc
Professional
Luc-Henri Dorsay, MEE, MBME, MHIT, MBHA, ID-Ph.D
Senior Executive Consultant
9 Brindle Way, Suite 305
Toronto ON K7R4B9
Canada
luc-henri.dorsay@vextorian.example
www.vextorian.example
We require the following in our pack: Business cards, fax cover sheets, letterheads, envelopes, CD cases & labels, Email signatures,
Business Consulting and Professional Services Portfolio:
- eHealth consulting and research
- Healthcare IT project management
- Biomedical and health informatics
- Hospital and clinical engineering
- Business analysis and management
- Clean energy and technology management
- eLearning and knowledge translation

```html
<!DOCTYPE html>
<html lang="en">
<head>
<meta charset="utf-8">
<title>Vextorian Group – Stationery Pack</title>
<link href="https://fonts.googleapis.com/css2?family=Montserrat:wght@400;600;700&display=swap" rel="stylesheet">
<style>
  :root {
    --stage-top: #3a3a3a;
    --stage-bottom: #1f1f1f;
    --paper: #ffffff;
    --paper-shade: #e9ecef;
    --ink: #4a4f55;
    --ink-soft: #8a9097;
    --brand-green: #8cc63f;
    --brand-blue: #1f8fd2;
    --brand-blue-dark: #146aa0;
    --card-dark: #262a2e;
    --label: #9a9a9a;
  }
  * { box-sizing: border-box; margin: 0; padding: 0; }
  html, body { width: 1200px; height: 310px; overflow: hidden; }
  body {
    position: relative;
    font-family: "Montserrat", Arial, sans-serif;
    background: radial-gradient(ellipse at 40% 30%, var(--stage-top), var(--stage-bottom));
    color: var(--ink);
  }
  .piece { position: absolute; background: var(--paper); box-shadow: 0 2px 6px rgba(0,0,0,.5); overflow: hidden; }
  .caption { position: absolute; font-size: 6px; color: var(--label); text-align: center; }
  .wordmark { display: flex; align-items: center; gap: 4px; font-weight: 700; letter-spacing: .08em; color: var(--brand-blue); }
  .wordmark .dot { width: 1em; height: 1em; border-radius: 50%; background: var(--brand-green); flex: none; }
  .wordmark small { display: block; font-size: .45em; letter-spacing: .3em; font-weight: 600; }

  .stage-mark { position: absolute; left: 16px; top: 22px; font-size: 17px; color: #f2f2f2; }
  .stage-mark .dot { background: var(--brand-green); }

  .card { width: 68px; height: 44px; top: 106px; }
  .card--front { left: 19px; padding: 5px; }
  .card--front .wordmark { font-size: 6px; }
  .card--front .lines { margin-top: 6px; font-size: 3px; line-height: 1.5; color: var(--ink-soft); }
  .card--back { left: 92px; background: var(--card-dark); padding: 7px; color: #ccd; }
  .card--back .wordmark { font-size: 6px; color: #fff; }
  .card--back .lines { margin-top: 5px; font-size: 3px; line-height: 1.5; }

  .signature { left: 19px; top: 200px; width: 144px; height: 78px; display: flex; }
  .signature .side { width: 48px; padding: 6px 4px; }
  .signature .side .wordmark { font-size: 5px; }
  .signature .body { flex: 1; background: var(--brand-blue); color: #fff; padding: 6px; font-size: 3.4px; line-height: 1.6; }
  .signature .body b { font-size: 4.5px; }

  .letterhead { top: 12px; width: 120px; height: 262px; padding: 10px 9px; }
  .letterhead .wordmark { font-size: 7px; }
  .letterhead .contact { position: absolute; right: 9px; top: 10px; font-size: 3px; line-height: 1.5; color: var(--ink-soft); text-align: right; }
  .letterhead .rule { height: 1px; background: var(--brand-green); margin-top: 10px; }
  .letterhead .foot { position: absolute; left: 9px; right: 9px; bottom: 8px; height: 2px; background: linear-gradient(90deg, var(--brand-green), var(--brand-blue)); }
  .lh-1 { left: 305px; }
  .lh-2 { left: 440px; }

  .fax { left: 600px; top: 12px; width: 205px; height: 150px; padding: 10px; }
  .fax .wordmark { font-size: 8px; }
  .fax .title { margin-top: 8px; font-size: 5px; font-weight: 600; color: var(--brand-blue); }
  .fax .row { margin-top: 5px; height: 1px; background: var(--paper-shade); }
  .slip { left: 600px; top: 180px; width: 205px; height: 95px; padding: 10px; }
  .slip .wordmark { font-size: 8px; }
  .slip .note { margin-top: 10px; font-size: 4px; color: var(--ink-soft); }

  .envelope { left: 960px; width: 160px; height: 66px; padding: 7px; }
  .envelope .wordmark { font-size: 6px; }
  .envelope svg { position: absolute; inset: 0; }
  .env-green { top: 12px; background: var(--brand-green); }
  .env-green .wordmark { color: #fff; position: relative; }
  .env-blue { top: 88px; }
  .env-white { top: 164px; }
</style>
</head>
<body>
  <div class="wordmark stage-mark"><span class="dot"></span><span>VEXTORIAN<small>GROUP</small></span></div>

  <section class="piece card card--front">
    <div class="wordmark"><span class="dot"></span>VEXTORIAN</div>
    <div class="lines">Luc-Henri Dorsay<br>Senior Executive Consultant<br>9 Brindle Way, Suite 305<br>www.vextorian.example</div>
  </section>
  <section class="piece card card--back">
    <div class="wordmark"><span class="dot"></span>VEXTORIAN</div>
    <div class="lines">Consulting &amp; Professional Services<br>Toronto ON K7R4B9</div>
  </section>
  <p class="caption" style="left:19px;top:158px;width:144px">Business Cards</p>

  <section class="piece signature">
    <div class="side"><div class="wordmark"><span class="dot"></span>VEXTORIAN</div></div>
    <div class="body"><b>Luc-Henri Dorsay</b><br>Senior Executive Consultant<br>luc-henri.dorsay@vextorian.example<br>www.vextorian.example<br>9 Brindle Way, Suite 305<br>Toronto ON K7R4B9 Canada</div>
  </section>
  <p class="caption" style="left:19px;top:284px;width:144px">Email Signature</p>

  <section class="piece letterhead lh-1">
    <div class="wordmark"><span class="dot"></span>VEXTORIAN</div>
    <div class="contact">9 Brindle Way, Suite 305<br>Toronto ON K7R4B9<br>www.vextorian.example</div>
    <div class="rule"></div><div class="foot"></div>
  </section>
  <p class="caption" style="left:305px;top:280px;width:120px">Letterhead</p>
  <section class="piece letterhead lh-2">
    <div class="wordmark"><span class="dot"></span>VEXTORIAN</div>
    <div class="contact">9 Brindle Way, Suite 305<br>Toronto ON K7R4B9<br>www.vextorian.example</div>
    <div class="rule"></div><div class="foot"></div>
  </section>
  <p class="caption" style="left:440px;top:280px;width:120px">Second Page</p>

  <section class="piece fax">
    <div class="wordmark"><span class="dot"></span>VEXTORIAN</div>
    <div class="title">Fax Cover Sheet</div>
    <div class="row"></div><div class="row"></div><div class="row"></div><div class="row"></div>
  </section>
  <p class="caption" style="left:600px;top:167px;width:205px">Fax Cover</p>
  <section class="piece slip">
    <div class="wordmark"><span class="dot"></span>VEXTORIAN</div>
    <div class="note">With compliments</div>
  </section>
  <p class="caption" style="left:600px;top:280px;width:205px">Compliment Slip</p>

  <section class="piece envelope env-green">
    <div class="wordmark"><span class="dot" style="background:#fff"></span>VEXTORIAN</div>
  </section>
  <section class="piece envelope env-blue">
    <svg width="160" height="66" viewBox="0 0 160 66" aria-hidden="true"><path d="M0 0H160V30L80 50L0 30Z" fill="var(--brand-blue)"/></svg>
  </section>
  <section class="piece envelope env-white">
    <svg width="160" height="66" viewBox="0 0 160 66" aria-hidden="true"><path d="M0 0L80 36L160 0" fill="none" stroke="var(--paper-shade)" stroke-width="1"/></svg>
    <div class="wordmark" style="position:relative"><span class="dot"></span>VEXTORIAN</div>
  </section>
  <p class="caption" style="left:960px;top:236px;width:160px">Envelopes</p>
</body>
</html>
```